Quorvex clinic business card - double sided for young clinic

I require business cards for my aesthetic clinic specialising in the below treatments. I would like the cards to be modern as my clinic base are young 22-35 years old. I require my logo on it and would like the edges to be rounded.

I have an aesthetic clinic specialising in :
Quorvex
Lip Enhancement
Chemical Peels
Facial Fillers
Non Surgical Face Lift

I would the cards to have the following information on them:
My logo - (in grey/silver)
address
Phone number
services

Colours :
White/grey/silver and red

a nice image on there, perhaps a set of lips as this is a main service i deliver

Company Name: PDA Address: 52 Farrowmere Road, 4 Brackwell High Street, KT9 4WQ Phone: 0208 794 2160 Website: www.penningtondoweaesthetics.co.uk

Target Market(s)

clinics 22-45 years old mainly female

Industry/Entity Type

Business

Contact Information for Business Card

as above

Requirements
Must have
• logo
• Address
• Email
• Phone number
• Services i offer
Nice to have
• images

```html
<!DOCTYPE html>
<html lang="en">
<head>
<meta charset="utf-8">
<title>Pennington Dowe Aesthetics – Business Card</title>
<link rel="stylesheet" href="https://fonts.googleapis.com/css2?family=Cinzel:wght@400&family=Open+Sans:ital,wght@0,400;0,600;0,700;1,400&display=swap">
<style>
  :root {
    --page: #d9d6d1;
    --card-white: #f4f4f4;
    --card-grey: #dcdcdc;
    --ink-dark: #4a4a4a;
    --ink-mid: #6f6f6f;
    --ink-light: #9a9a9a;
    --black: #0b0b0b;
    --black-soft: #2a2a2a;
    --silver: #bdbdbd;
    --red: #d0203a;
    --lip-red: #9e2a3a;
    --white: #ffffff;
  }
  * { box-sizing: border-box; margin: 0; padding: 0; }
  html, body { width: 1200px; height: 1062px; overflow: hidden; }
  body {
    background: var(--page);
    font-family: "Open Sans", Arial, sans-serif;
    position: relative;
  }
  .card {
    position: absolute;
    left: 180px;
    width: 840px;
    height: 480px;
    border-radius: 18px;
    overflow: hidden;
    box-shadow: 0 8px 22px rgba(0,0,0,0.28);
  }

  /* ---------- Front ---------- */
  .card-front {
    top: 34px;
    background: radial-gradient(ellipse at 45% 40%, var(--white) 0%, var(--card-white) 55%, var(--card-grey) 100%);
  }
  .front-wave { position: absolute; inset: 0; width: 100%; height: 100%; }
  .brand {
    position: absolute;
    left: 84px;
    top: 112px;
    display: flex;
    align-items: center;
    gap: 18px;
  }
  .brand-circle {
    width: 100px; height: 100px;
    border-radius: 50%;
    background: var(--ink-mid);
    flex: none;
  }
  .brand-name {
    font-family: "Cinzel", Georgia, serif;
    font-weight: 400;
    color: var(--ink-mid);
    line-height: 1.15;
    letter-spacing: 1.5px;
    white-space: nowrap;
  }
  .brand-name .line-1 { display: block; font-size: 19px; }
  .brand-name .line-2 { display: block; font-size: 31px; letter-spacing: 3px; }
  .divider {
    position: absolute;
    left: 488px; top: 122px;
    width: 1px; height: 80px;
    background: linear-gradient(to bottom, transparent, var(--ink-dark), transparent);
  }
  .contacts {
    position: absolute;
    left: 506px; top: 117px;
    list-style: none;
    color: var(--ink-mid);
    font-size: 13.5px;
    line-height: 30px;
  }
  .contacts li { display: flex; align-items: center; gap: 9px; white-space: nowrap; }
  .contacts svg, .address svg { width: 13px; height: 13px; flex: none; }
  .address {
    position: absolute;
    left: 84px; top: 236px;
    display: flex;
    align-items: center;
    gap: 9px;
    color: var(--ink-mid);
    font-size: 13.5px;
    white-space: nowrap;
  }
  .person {
    position: absolute;
    left: 60px; top: 300px;
    color: var(--ink-mid);
  }
  .person-name { font-size: 30px; font-weight: 600; line-height: 1.1; }
  .person-role { font-size: 20px; color: var(--ink-light); }

  /* ---------- Back ---------- */
  .card-back {
    top: 548px;
    background: radial-gradient(ellipse at 55% 55%, var(--black-soft) 0%, var(--black) 70%);
  }
  .back-heading {
    position: absolute;
    left: 44px; top: 36px;
    color: var(--white);
    font-size: 24px;
    font-weight: 700;
    font-style: italic;
    letter-spacing: -0.3px;
  }
  .services {
    position: absolute;
    left: 64px; top: 92px;
    list-style: none;
    color: var(--white);
    font-size: 22px;
    line-height: 34px;
  }
  .services li { position: relative; padding-left: 20px; }
  .services li::before {
    content: "";
    position: absolute;
    left: 0; top: 14px;
    width: 6px; height: 6px;
    border-radius: 50%;
    background: var(--red);
  }
  .lips-image {
    position: absolute;
    left: 340px; top: 200px;
    width: 230px; height: 140px;
    border-radius: 50%;
    background: radial-gradient(ellipse at center, var(--lip-red) 0%, rgba(120,25,40,0.55) 45%, rgba(11,11,11,0) 75%);
  }
  .back-brand {
    position: absolute;
    right: 56px; bottom: 44px;
    display: flex;
    align-items: center;
    gap: 18px;
  }
  .back-brand .brand-circle { width: 88px; height: 88px; background: var(--silver); }
  .back-brand .brand-name { color: var(--silver); }
  .back-brand .brand-name .line-1 { font-size: 17px; }
  .back-brand .brand-name .line-2 { font-size: 28px; }
</style>
</head>
<body>

  <section class="card card-front" aria-label="Business card front">
    <svg class="front-wave" viewBox="0 0 840 480" preserveAspectRatio="none" aria-hidden="true">
      <defs>
        <linearGradient id="waveBlack" x1="0" y1="0" x2="1" y2="0">
          <stop offset="0" stop-color="#3a3a3a"/>
          <stop offset="0.5" stop-color="#0b0b0b"/>
          <stop offset="1" stop-color="#000"/>
        </linearGradient>
      </defs>
      <path d="M0 480 L0 455 C180 450 360 420 520 360 C640 315 720 300 840 296 L840 480 Z" fill="url(#waveBlack)"/>
      <path d="M0 452 C180 446 360 414 520 354 C640 309 720 292 840 288" fill="none" stroke="#c8c8c8" stroke-width="6"/>
      <path d="M0 444 C180 438 360 406 520 346 C640 301 720 284 840 280" fill="none" stroke="#9a9a9a" stroke-width="2"/>
    </svg>

    <div class="brand">
      <div class="brand-circle" aria-hidden="true"></div>
      <div class="brand-name">
        <span class="line-1">PENNINGTON DOWE</span>
        <span class="line-2">AESTHETICS</span>
      </div>
    </div>

    <div class="divider" aria-hidden="true"></div>

    <ul class="contacts">
      <li>
        <svg viewBox="0 0 16 16" aria-hidden="true"><path d="M4 1.5 L6.5 4.5 L5 6 C5.8 8 7.8 10.2 10 11 L11.5 9.5 L14.5 12 L12.8 14.3 C7 13.5 2.5 9 1.7 3.2 Z" fill="#4a4a4a"/></svg>
        0208 794 2160
      </li>
      <li>
        <svg viewBox="0 0 16 16" aria-hidden="true"><g fill="none" stroke="#4a4a4a" stroke-width="1.3"><circle cx="8" cy="8" r="6.5"/><ellipse cx="8" cy="8" rx="3" ry="6.5"/><path d="M1.5 8 H14.5 M2.5 4.8 H13.5 M2.5 11.2 H13.5"/></g></svg>
        www.penningtondoweaesthetics.co.uk
      </li>
      <li>
        <svg viewBox="0 0 16 16" aria-hidden="true"><g fill="none" stroke="#1a1a1a" stroke-width="1.8"><circle cx="8" cy="8" r="2.6"/><path d="M10.6 6 V9.3 C10.6 11 13.8 11 13.8 8 A5.8 5.8 0 1 0 11.3 12.8"/></g></svg>
        hello@penningtondowe.co.uk
      </li>
    </ul>

    <p class="address">
      <svg viewBox="0 0 16 16" aria-hidden="true"><path d="M8 1 C5 1 3 3.2 3 6 C3 9.5 8 15 8 15 C8 15 13 9.5 13 6 C13 3.2 11 1 8 1 Z M8 4 A2 2 0 1 1 8 8 A2 2 0 1 1 8 4 Z" fill="#4a4a4a" fill-rule="evenodd"/></svg>
      52 Farrowmere Road, 4 Brackwell High Street, KT9 4WQ
    </p>

    <div class="person">
      <p class="person-name">Marcus Hale</p>
      <p class="person-role">Manager</p>
    </div>
  </section>

  <section class="card card-back" aria-label="Business card back">
    <p class="back-heading">I have an aesthetic clinic specialising in :</p>
    <ul class="services">
      <li>Quorvex</li>
      <li>Lip Enhancement</li>
      <li>Chemical Peels</li>
      <li>Facial Fillers</li>
      <li>Non Surgical Face Lift</li>
    </ul>
    <div class="lips-image" role="img" aria-label="Soft red image of a pair of lips"></div>
    <div class="back-brand">
      <div class="brand-circle" aria-hidden="true"></div>
      <div class="brand-name">
        <span class="line-1">PENNINGTON DOWE</span>
        <span class="line-2">AESTHETICS</span>
      </div>
    </div>
  </section>

</body>
</html>
```